Kiss Wed or Run Show Flyer 2017

We are 3 female comedians who need to brand a new show that we want to take on the road. The show will be geared towards relationships. We will perform at clubs and theaters. We will also end up needing a logo etc for tee shirts and business cards and website. Etc. I am including some photos of the 3 of us from an old flyer from another show we did together ... it's not 'great' but it shows the 3 of us. ... perhaps there would be room for headshots also? or maybe we would add one shot of the 3 of us? There's also a chance we might want to include a 'guest' once in a while. The flyer should include space for the venue details and time date etc. and website. www.kisswedorrun-demo.net

Target Market(s)

Women. PG 13 and up. but not boxed in for just women. guys will have HUGE FUN TOO.

Logo Text

'Kiss Wed or Run'

Font styles to use
Sans Serif

Colors
e667a6
f04a50

Requirements
Must have
• Kiss Wed or Run
• possible tag lines- '3 comedians looking for love and finding the funny' or 'love means never having to say you're funny' or '3 funny women with choices'
• (we are still ironing out exactly the lines)
• names of 3 comedians: Nadia Pruitt, Odette Rue, Tessa Kolby
• space to easily edit venue name - date - time
Should not have
• no swirly bits. it should look strong and powerful but feminine.

```html
<!DOCTYPE html>
<html lang="en">
<head>
<meta charset="utf-8">
<title>Kiss Wed or Run – Show Flyer</title>
<link href="https://fonts.googleapis.com/css2?family=Oswald:wght@300;400;500&family=Fredoka:wght@600&family=Gabriela&display=swap" rel="stylesheet">
<style>
  :root {
    --red: #f04a50;
    --red-deep: #e5434b;
    --pink: #e667a6;
    --pink-hot: #e0479a;
    --pink-soft: #f6c6de;
    --mauve: #c9799f;
    --blush: #fbe6f0;
    --paper: #ffffff;
  }
  * { margin: 0; padding: 0; box-sizing: border-box; }
  html, body { width: 1000px; height: 1200px; overflow: hidden; background: var(--paper); }
  .canvas { position: relative; width: 1000px; height: 1200px; background: var(--paper); }

  .flyer {
    position: absolute; left: 97px; top: 48px; width: 808px; height: 1114px;
    overflow: hidden; background: var(--paper);
  }
  .flyer__backdrop {
    position: absolute; inset: 0;
    background:
      radial-gradient(ellipse 70% 28% at 50% 58%, rgba(255,255,255,0.95), rgba(255,255,255,0) 70%),
      linear-gradient(180deg, var(--pink-hot) 0%, #e77ab3 24%, #f2b2d2 38%, var(--blush) 50%, #fdf3f8 70%, #fbeef4 100%);
  }
  .flyer__portraits {
    position: absolute; left: 48px; top: 67px; width: 715px; height: 305px;
    border-radius: 150px 150px 24px 24px;
    background: linear-gradient(180deg, var(--mauve) 0%, #d98fb4 60%, #ecb3cf 100%);
  }

  .cast__name {
    position: absolute; top: 384px; width: 240px; margin-left: -120px;
    font-family: "Fredoka", sans-serif; font-weight: 600; color: var(--red);
    text-align: center; line-height: 1;
  }
  .cast__name--left { left: 190px; }
  .cast__name--centre { left: 413px; }
  .cast__name--right { left: 646px; }
  .cast__first { display: block; font-size: 22px; margin-bottom: 4px; }
  .cast__last { display: block; font-size: 38px; }

  .brand-mark {
    position: absolute; left: 140px; top: 565px; width: 150px; height: 150px;
    border-radius: 50%; background: var(--pink-soft);
  }
  .title {
    position: absolute; left: 343px; top: 491px;
    font-family: "Oswald", sans-serif; color: var(--red); text-transform: uppercase;
    font-weight: 400;
  }
  .title__line { display: block; font-size: 95px; line-height: 88px; height: 88px; letter-spacing: 1px; white-space: nowrap; }
  .title__line--outline { font-weight: 300; color: transparent; -webkit-text-stroke: 3px var(--red); }

  .tagline {
    position: absolute; left: 0; top: 770px; width: 100%; padding-left: 20px;
    text-align: center; font-family: "Gabriela", serif; font-size: 21px; color: var(--red-deep);
  }
  .tagline__num { font-size: 30px; }

  .details { position: absolute; left: 0; top: 838px; width: 100%; text-align: center; font-family: "Oswald", sans-serif; color: var(--red); }
  .details__date { font-size: 40px; font-weight: 500; line-height: 1.05; }
  .details__venue { font-size: 29px; font-weight: 500; line-height: 1.2; }

  .guests { position: absolute; left: 0; top: 945px; width: 100%; text-align: center; font-family: "Oswald", sans-serif; color: var(--red); }
  .guests__heading { font-size: 34px; font-weight: 500; line-height: 1.2; }
  .guests__list { list-style: none; display: flex; justify-content: center; margin-top: 6px; }
  .guests__item { font-size: 24px; font-weight: 300; line-height: 1.5; }
  .guests__item + .guests__item::before { content: "•"; margin: 0 30px; font-weight: 500; }

  .website {
    position: absolute; left: 0; top: 1082px; width: 100%; text-align: center;
    font-family: "Oswald", sans-serif; font-weight: 400; font-size: 17px; letter-spacing: 1px; color: var(--red);
  }
</style>
</head>
<body>
<div class="canvas">
  <section class="flyer">
    <div class="flyer__backdrop" role="img" aria-label="Pink mosaic tile pattern fading to white"></div>
    <div class="flyer__portraits" role="img" aria-label="Headshot photograph of the three comedians side by side"></div>

    <p class="cast__name cast__name--left"><span class="cast__first">Nadia</span><span class="cast__last">Pruitt</span></p>
    <p class="cast__name cast__name--centre"><span class="cast__first">Odette</span><span class="cast__last">Rue</span></p>
    <p class="cast__name cast__name--right"><span class="cast__first">Tessa</span><span class="cast__last">Kolby</span></p>

    <div class="brand-mark" aria-hidden="true"></div>
    <h1 class="title">
      <span class="title__line">Kiss</span>
      <span class="title__line">Wed</span>
      <span class="title__line title__line--outline">or Run</span>
    </h1>

    <p class="tagline"><span class="tagline__num">3</span> Comedians looking for love &amp; finding the funny</p>

    <div class="details">
      <p class="details__date">Saturday, December 17, 2016 At 9PM</p>
      <p class="details__venue">Boston, 9th Avenue, Lakeside Crown Hall</p>
    </div>

    <div class="guests">
      <h2 class="guests__heading">- Guests -</h2>
      <ul class="guests__list">
        <li class="guests__item">Greta Lindqvist</li>
        <li class="guests__item">Marcus Pell</li>
        <li class="guests__item">Judith Orme</li>
      </ul>
      <ul class="guests__list">
        <li class="guests__item">Rosa Keane</li>
        <li class="guests__item">Felix Dorne</li>
      </ul>
    </div>

    <p class="website">www.kisswedorrun-demo.net</p>
  </section>
</div>
</body>
</html>
```